models required for semi permeanant eyebrow treatment

The flyer design needs to be simple and not too much fuss.
I would like to specify that im completing my training with maria loddon velvet arch which is the leading training team in semi permeanant makeup and I require models for hairstroke eyebrow treatment . The charge is £100 and potential clients would require to consultation prior to the treatment
my contact details including my email and telephone number should be included
holly
07712036984

Industry/Entity Type

Training

Requirements
Nice to have
• Because im already attaching a before and after photo I thinknto add any other sketches would make the flyer to cluttered so just to keep it simple and to the point and neat and structured but at the same time quiete pretty and feminine

```html
<!DOCTYPE html>
<html lang="en">
<head>
<meta charset="utf-8">
<title>Models Required – Hairstroke Eyebrow Treatment</title>
<link rel="stylesheet" href="https://fonts.googleapis.com/css2?family=Questrial&family=Didact+Gothic&display=swap">
<style>
  :root {
    --ink: #000000;
    --paper: #ffffff;
    --coral: #f7816a;
    --band: #f99a85;
    --photo-dark: #5a4e48;
    --photo-light: #a89a90;
  }
  * { margin: 0; padding: 0; box-sizing: border-box; }
  html, body { width: 962px; height: 1200px; overflow: hidden; background: var(--ink); }
  .flyer {
    position: relative;
    width: 962px;
    height: 1200px;
    background: var(--ink);
    color: var(--paper);
    font-family: "Questrial", "Didact Gothic", sans-serif;
  }
  .headline {
    position: absolute;
    top: 128px;
    left: 0;
    width: 100%;
    text-align: center;
    line-height: 1;
  }
  .headline span { display: block; }
  .headline .lead {
    color: var(--coral);
    font-size: 58px;
    font-weight: 700;
    letter-spacing: 1px;
    -webkit-text-stroke: 1.4px var(--coral);
  }
  .headline .mid {
    font-size: 58px;
    margin-top: 12px;
    letter-spacing: 1px;
  }
  .headline .sub {
    font-size: 46px;
    margin-top: 16px;
    letter-spacing: 1px;
  }
  .band {
    position: absolute;
    top: 510px;
    left: 0;
    width: 100%;
    height: 88px;
    background: var(--band);
  }
  .before-after {
    position: absolute;
    top: 425px;
    left: 322px;
    width: 273px;
    height: 263px;
    border: 2px solid var(--paper);
    background: var(--paper);
    display: flex;
    flex-direction: column;
    gap: 2px;
  }
  .before-after .shot {
    flex: 1;
    background: linear-gradient(180deg, var(--photo-dark), var(--photo-light) 55%, var(--photo-dark));
  }
  .intro {
    position: absolute;
    top: 770px;
    left: 80px;
    width: 802px;
    text-align: center;
    font-size: 26px;
    line-height: 37px;
  }
  .contact {
    position: absolute;
    top: 1020px;
    left: 0;
    width: 100%;
    text-align: center;
  }
  .contact .name { font-size: 34px; line-height: 1; }
  .contact .rule {
    position: absolute;
    top: 55px;
    height: 3px;
    background: var(--band);
  }
  .contact .rule.left { left: 0; width: 376px; }
  .contact .rule.right { left: 584px; width: 378px; }
  .contact .phone { font-size: 24px; margin-top: 16px; letter-spacing: 1px; }
</style>
</head>
<body>
  <main class="flyer">
    <h1 class="headline">
      <span class="lead">“RQUIRE MODELS</span>
      <span class="mid">FOR HAIRSTRAKE</span>
      <span class="sub">EYEBROW TREATMENT”</span>
    </h1>

    <div class="band"></div>

    <div class="before-after">
      <div class="shot" role="img" aria-label="After photo: eyes with finished hairstroke eyebrows"></div>
      <div class="shot" role="img" aria-label="Before photo: eyes with natural eyebrows before treatment"></div>
    </div>

    <p class="intro">I’m completing my training with maria loddon velvet arch which is the leading training team in semi permeanant makeup and I require models for hairstroke eyebrow treatment .The charge is £100 and potential clients would require to consultation prior to the treatment</p>

    <div class="contact">
      <p class="name">Holly</p>
      <span class="rule left"></span>
      <span class="rule right"></span>
      <p class="phone">07712036984</p>
    </div>
  </main>
</body>
</html>
```